Wine and retail website for a high-end resort community

We are introducing a line of quality wines in the resort community of Saltmarsh Ridge, Massachusetts, USA. The site will detail information about the wine, and online store connected to and external government approved shipper for wine, and additional non-alcoholic retail merchandise sales.

We are planning the site to be driven off the Squarespace platform so I do not believe coding is necessary initially; however, the ability to do sop would be helpful if needed.

Attached are the images/files we have available so far. Please feel free to use stock images in your design.

Target Market(s)

Wine enthusiasts in the resort community of Martha’s Vineyard Massachusetts

Industry/Entity Type

Wine

Number of Pages Required

4 page

Font styles to use
Sans Serif

Requirements
Must have
• Home page, about page, wine page, e-commerce page, retail merchandise page. I recently came across brenthollwines.com and really like the look and layout of their pages if that helps
Nice to have
• A short wine/Martha’s Vineyard related video on the home page

```html
<!DOCTYPE html>
<html lang="en">
<head>
<meta charset="utf-8">
<title>Saltmarsh Ridge Estates</title>
<link rel="stylesheet" href="https://fonts.googleapis.com/css2?family=Oswald:wght@700&family=Mulish:wght@400;600;700&family=Cormorant+Garamond:wght@500;600&display=swap">
<style>
:root{
  --maroon:#8b1e2f;
  --gold:#e3a522;
  --ink:#1f1f1f;
  --text:#333;
  --dark-panel:#262626;
  --band:#0b0b0b;
  --footer:#1c1416;
  --muted:#f3f3f3;
  --star:#f39a12;
}
*{box-sizing:border-box;margin:0;padding:0}
html,body{width:1200px;height:2966px;overflow:hidden;background:#fff}
.page{position:relative;width:1042px;height:2575.5px;transform:scale(1.15163);transform-origin:0 0;font-family:"Mulish",sans-serif;color:var(--text);overflow:hidden}
.abs{position:absolute}
.serif{font-family:"Cormorant Garamond",serif;font-weight:600}
.btn{position:absolute;display:flex;align-items:center;justify-content:center;font-family:"Mulish",sans-serif;font-weight:700;font-size:11px;letter-spacing:.3px;color:#fff;background:var(--gold)}
.btn.dark{color:#1a1a1a}
.btn.maroon{background:var(--maroon)}

/* header */
.hero-bg{left:0;top:0;width:1042px;height:700px;background:linear-gradient(180deg,#f7f7f7 0%,#fafafa 60%,#fff 100%)}
.logo{left:118px;top:28px;width:120px;text-align:center;color:#2a2a2a;line-height:1}
.logo .name{font-size:21px;letter-spacing:.3px}
.logo .sub{font-size:8.5px;letter-spacing:3px;margin-top:4px}
.nav{left:360px;top:45px;display:flex;gap:30px;font-size:11.5px;color:#333}
.nav .active{color:var(--maroon)}
.contact-top{left:763px;top:44px;display:flex;align-items:center;gap:6px;font-size:11.5px;color:#333}
.cart{left:886px;top:44px;display:flex;align-items:center;gap:4px;font-size:11.5px}

.hero-title{left:123px;top:180px;font-family:"Oswald",sans-serif;font-weight:700;font-size:70px;line-height:1;color:var(--maroon);letter-spacing:-.5px;transform:scaleX(.92);transform-origin:left}
.hero-sub{left:124px;top:258px;font-size:18.5px;line-height:23px;font-weight:600;color:#1a1a1a;width:360px}
.hero-art{left:470px;top:128px;width:572px;height:380px;background:radial-gradient(ellipse at 60% 60%,#cfcfcf 0%,#e6e6e6 45%,rgba(245,245,245,0) 72%)}
.hero-bottles{left:686px;top:134px;width:126px;height:272px;background:linear-gradient(90deg,#c98a2a 0%,#e7b362 40%,#2a0d12 55%,#120507 100%);border-radius:18px 18px 6px 6px}
.brush{left:40px;top:440px;width:1002px;height:260px;background:radial-gradient(ellipse at 50% 40%,rgba(190,190,190,.55) 0%,rgba(220,220,220,.35) 45%,rgba(255,255,255,0) 72%)}

/* about */
.about-card{left:123px;top:499px;width:240px;height:347px;background:#fff;box-shadow:0 12px 30px rgba(0,0,0,.12)}
.about-panel{left:362px;top:499px;width:557px;height:347px;background:var(--dark-panel)}
.about-photo{left:147px;top:522px;width:353px;height:301px;background:linear-gradient(180deg,#c7653b 0%,#8a3c25 35%,#4a2a14 60%,#1e140a 100%)}
.about-frame{left:164px;top:569px;width:385px;height:197px;border:1px solid var(--gold);border-right:none}
.about-eyebrow{left:552px;top:562px;font-size:14px;color:#fff}
.about-title{left:551px;top:572px;font-size:31px;color:#fff;letter-spacing:.5px}
.about-copy{left:552px;top:613px;width:330px;font-size:11.2px;line-height:20px;color:#ddd}

/* products */
.section-title{left:0;width:1042px;text-align:center;font-size:32px;color:#1a1a1a;letter-spacing:.3px}
.section-lead{left:300px;width:442px;text-align:center;font-size:11.5px;line-height:17px;color:#333}
.product-img{top:1016px;width:215px;height:235px;border-radius:50%}
.product-img.red{left:213px;background:radial-gradient(circle at 50% 50%,#5b2b33 0%,#c9a97a 30%,#f3e6ea 55%,rgba(255,255,255,0) 72%)}
.product-img.white{left:608px;background:radial-gradient(circle at 50% 50%,#d89a3a 0%,#d9c090 32%,#f8efdf 55%,rgba(255,255,255,0) 72%)}
.product-name{top:1260px;width:360px;text-align:center;font-size:23px;font-weight:500}
.product-copy{top:1292px;width:280px;text-align:center;font-size:11.2px;line-height:17px;color:#333}

/* approved band */
.band{left:0;top:1462px;width:1042px;height:312px;background:var(--band)}
.band-art{left:620px;top:1478px;width:305px;height:290px;background:radial-gradient(ellipse at 60% 45%,#8a6a1e 0%,#3a2a12 35%,#150c0c 60%,rgba(11,11,11,0) 75%)}
.band-title{left:124px;top:1533px;font-size:31px;line-height:35px;color:#fff;font-weight:500;letter-spacing:.4px}
.band-copy{left:124px;top:1608px;width:460px;font-size:14px;line-height:21px;color:#eee}

/* testimonials */
.quote-card{top:1905px;width:251px;height:178px;background:#fff;box-shadow:0 4px 18px rgba(0,0,0,.09);padding:36px 18px 0;font-size:11.2px;line-height:20px;color:#333}
.quote-tail{top:2082px;width:0;height:0;border-left:26px solid transparent;border-top:22px solid #fff}
.avatar{top:2089px;width:62px;height:62px;border-radius:50%;background:radial-gradient(circle at 50% 40%,#c9a58c 0%,#8f7563 55%,#3d3d3d 100%)}
.client{top:2104px;font-size:12.5px;font-weight:700;color:#1a1a1a}
.stars{top:2121px;font-size:10px;letter-spacing:2px;color:var(--star)}
.dots{left:482px;top:2176px;display:flex;gap:6px;align-items:center}
.dots span{width:10px;height:10px;border-radius:50%;background:#d6d6d6}
.dots .on{width:13px;height:13px;background:var(--maroon);box-shadow:0 0 0 2px #fff,0 0 0 3px var(--maroon)}

/* footer */
.footer{left:0;top:2263px;width:1042px;height:261px;background:repeating-linear-gradient(90deg,#1b1315 0 2px,#1f1719 2px 4px)}
.footer-logo{left:120px;top:2358px;width:132px;text-align:center;color:#fff;line-height:1}
.footer-logo .name{font-size:23px}
.footer-logo .sub{font-size:8.5px;letter-spacing:3px;margin-top:5px}
.socials{left:123px;top:2440px;display:flex;gap:10px}
.socials span{width:25px;height:25px;border:1px solid #bbb;border-radius:50%}
.foot-head{top:2336px;font-size:14.5px;color:#fff;letter-spacing:.4px}
.foot-links{left:296px;top:2369px;list-style:none;font-size:11.5px;color:#fff;line-height:21px}
.foot-links li::before{content:"»";margin-right:5px;font-weight:700}
.foot-item{left:483px;display:flex;gap:8px;font-size:11.2px;line-height:16px;color:#fff}
.foot-item svg{flex:none;margin-top:1px}
.news-copy{left:699px;top:2369px;width:210px;font-size:11.2px;line-height:16px;color:#fff}
.news-input{left:699px;top:2412px;width:188px;height:34px;background:#fff;font-size:11.5px;color:#333;padding:10px 12px}
.news-btn{left:886px;top:2412px;width:34px;height:34px;background:var(--maroon);display:flex;align-items:center;justify-content:center}
.copyright{left:0;top:2524px;width:1042px;height:52px;background:var(--maroon);color:#fff;font-size:11.5px;display:flex;align-items:center;justify-content:center}
</style>
</head>
<body>
<div class="page">

  <!-- header & hero -->
  <div class="abs hero-bg"></div>
  <div class="abs brush" role="img" aria-label="Soft grey ink wash of coastline"></div>
  <div class="abs hero-art" role="img" aria-label="Sketched island map with rocky shore and lighthouse"></div>
  <div class="abs hero-bottles" role="img" aria-label="Bottles of white and red wine"></div>

  <div class="abs logo serif">
    <div class="name">SALTMARSH<br>RIDGE</div>
    <div class="sub">ESTATES</div>
  </div>

  <nav class="abs nav">
    <span class="active">HOME</span><span>ABOUT</span><span>WINE</span><span>SHOP</span><span>RETAIL MERCHANDISE</span>
  </nav>
  <div class="abs contact-top">
    <svg width="16" height="16" viewBox="0 0 24 24"><path fill="var(--maroon)" d="M6.6 10.8a15 15 0 006.6 6.6l2.2-2.2a1 1 0 011-.25 11.4 11.4 0 003.6.57 1 1 0 011 1V20a1 1 0 01-1 1A17 17 0 013 4a1 1 0 011-1h3.5a1 1 0 011 1c0 1.25.2 2.45.57 3.57a1 1 0 01-.25 1z"/></svg>
    <span>+1 123 456 7890</span>
  </div>
  <div class="abs cart">
    <svg width="17" height="16" viewBox="0 0 24 24"><path fill="var(--maroon)" d="M7 18a2 2 0 100 4 2 2 0 000-4zm10 0a2 2 0 100 4 2 2 0 000-4zM1 2h3.3l.9 2H21a1 1 0 01.9 1.4l-3.6 6.5a2 2 0 01-1.75 1.1H8.1l-.9 1.6V15h12v2H7a2 2 0 01-1.75-3L6.6 11.6 3 4H1z"/></svg>
    <span>(0)</span>
  </div>

  <h1 class="abs hero-title">WE SELL WINE</h1>
  <p class="abs hero-sub">In The Resort Community of Saltmarsh Ridge Massachusetts, USA</p>
  <a class="btn" style="left:123px;top:326px;width:101px;height:30px">SHOP NOW</a>

  <!-- about -->
  <div class="abs about-card"></div>
  <div class="abs about-panel"></div>
  <div class="abs about-photo" role="img" aria-label="Grapevine leaves at sunset over the vineyard"></div>
  <div class="abs about-frame"></div>
  <div class="abs about-eyebrow">ABOUT</div>
  <h2 class="abs about-title serif">SALTMARSH RIDGE</h2>
  <p class="abs about-copy">Lorem ipsum dolor sit amet, consectetuer adipiscing elit, sed diam nonummy nibh euismod tincidunt ut laoreet dolore mag na aliquam erat volutpat.<br>Ut wisi enim ad minim veniam, quis nostrud exerci tation ulla mc orper suscipit lobortis nisl ut aliquip ex ea commodo cons equat. Duis autem vel eum iriure dolor in hendrerit.</p>
  <a class="btn" style="left:552px;top:751px;width:101px;height:30px">READ MORE</a>

  <!-- products -->
  <h2 class="abs section-title serif" style="top:910px">OUR PRODUCTS</h2>
  <p class="abs section-lead" style="top:955px">Lorem ipsum dolor sit amet, consectetuer adipiscing elit, sed diam nonummy nibh euismod tincidunt ut laoreet dolore mag na aliquam erat volutpat.</p>

  <div class="abs product-img red" role="img" aria-label="Cabernet Sauvignon bottle with wooden gift box and dark grapes"></div>
  <h3 class="abs product-name serif" style="left:141px;color:var(--maroon)">Cabernet Sauvignon</h3>
  <p class="abs product-copy" style="left:184px">Lorem ipsum dolor sit amet, consectetuer adipiscing elit, sed diam nonummy nibh euismod tincidunt ut laoreet dolore magnaaliqu.</p>
  <a class="btn maroon" style="left:271px;top:1357px;width:102px;height:30px">SHOP NOW</a>

  <div class="abs product-img white" role="img" aria-label="Chardonnay bottle with wooden gift box and green grapes"></div>
  <h3 class="abs product-name serif" style="left:540px;color:var(--gold)">Chardonnay</h3>
  <p class="abs product-copy" style="left:580px">Lorem ipsum dolor sit amet, consectetuer adipiscing elit, sed diam nonummy nibh euismod tincidunt ut laoreet dolore magnaaliqu.</p>
  <a class="btn" style="left:669px;top:1357px;width:102px;height:30px">SHOP NOW</a>

  <!-- approved shipper -->
  <div class="abs band"></div>
  <div class="abs band-art" role="img" aria-label="Wine bottles, glass and grapes beside an approval seal"></div>
  <h2 class="abs band-title serif">AUTHORIZED GOVERNMENT<br>APPROVED SHIPPER FOR WINES</h2>
  <p class="abs band-copy">Lorem ipsum dolor sit amet, consectetuer adipiscing elit, sed diam nonummy nibh euismod tincidunt ut laoreet dolore magna aliquam erat</p>
  <a class="btn dark" style="left:123px;top:1668px;width:102px;height:30px">KNOW MORE</a>

  <!-- testimonials -->
  <h2 class="abs section-title serif" style="top:1842px">WHAT OUR HAPPY CLIENTS SAY</h2>

  <div class="abs quote-card" style="left:123px">Lorem ipsum dolor sit amet, consectetuer adipiscing elit, sed diam nonummy nibh euismod tincidunt ut laoreet dolore mag na aliquam erat volutpat. Ut wisi enim ad minim veniam, quis aflotli nostrud exerci tation ulla mc orper tincidu suscipit numm</div>
  <div class="abs quote-tail" style="left:128px"></div>
  <div class="abs avatar" style="left:166px" role="img" aria-label="Client portrait"></div>
  <div class="abs client" style="left:237px">ROWAN A.</div>
  <div class="abs stars" style="left:237px">★★★★★</div>

  <div class="abs quote-card" style="left:396px">Lorem ipsum dolor sit amet, consectetuer adipiscing elit, sed diam nonummy nibh euismod tincidunt ut laoreet dolore mag na aliquam erat volutpat. Ut wisi enim ad minim veniam, quis aflotli nostrud exerci tation ulla mc orper tincidu suscipit numm</div>
  <div class="abs quote-tail" style="left:401px"></div>
  <div class="abs avatar" style="left:439px" role="img" aria-label="Client portrait"></div>
  <div class="abs client" style="left:510px">CELIA M.</div>
  <div class="abs stars" style="left:510px">★★★★★</div>

  <div class="abs quote-card" style="left:668px">Lorem ipsum dolor sit amet, consectetuer adipiscing elit, sed diam nonummy nibh euismod tincidunt ut laoreet dolore mag na aliquam erat volutpat. Ut wisi enim ad minim veniam, quis aflotli nostrud exerci tation ulla mc orper tincidu suscipit numm</div>
  <div class="abs quote-tail" style="left:673px"></div>
  <div class="abs avatar" style="left:711px" role="img" aria-label="Client portrait"></div>
  <div class="abs client" style="left:782px">HOLLIS C.</div>
  <div class="abs stars" style="left:782px">★★★★★</div>

  <div class="abs dots"><span></span><span></span><span class="on"></span><span></span><span></span></div>

  <!-- footer -->
  <div class="abs footer"></div>
  <div class="abs footer-logo serif">
    <div class="name">SALTMARSH<br>RIDGE</div>
    <div class="sub">ESTATES</div>
  </div>
  <div class="abs socials"><span></span><span></span><span></span><span></span></div>

  <h4 class="abs foot-head serif" style="left:296px">QUICK LINKS</h4>
  <ul class="abs foot-links">
    <li>HOME</li><li>ABOUT</li><li>WINE</li><li>SHOP</li><li>RETAIL MERCHANDISE</li>
  </ul>

  <h4 class="abs foot-head serif" style="left:483px">CONTACT DETAILS</h4>
  <div class="abs foot-item" style="top:2369px">
    <svg width="16" height="16" viewBox="0 0 24 24" fill="none" stroke="#fff" stroke-width="1.6"><path d="M12 22s7-7 7-12a7 7 0 10-14 0c0 5 7 12 7 12z"/><circle cx="12" cy="10" r="2.5"/></svg>
    <span>123, Building Name, Street<br>City, State XY 123456</span>
  </div>
  <div class="abs foot-item" style="top:2417px">
    <svg width="16" height="16" viewBox="0 0 24 24" fill="none" stroke="#fff" stroke-width="1.6"><path d="M6.6 10.8a15 15 0 006.6 6.6l2.2-2.2a1 1 0 011-.25 11.4 11.4 0 003.6.57 1 1 0 011 1V20a1 1 0 01-1 1A17 17 0 013 4a1 1 0 011-1h3.5a1 1 0 011 1c0 1.25.2 2.45.57 3.57a1 1 0 01-.25 1z"/></svg>
    <span>+1 123 456 7890</span>
  </div>
  <div class="abs foot-item" style="top:2449px">
    <svg width="16" height="16" viewBox="0 0 24 24" fill="none" stroke="#fff" stroke-width="1.6"><rect x="3" y="5" width="18" height="14" rx="1.5"/><path d="M3 6l9 7 9-7"/></svg>
    <span>info@saltmarshridge.com</span>
  </div>

  <h4 class="abs foot-head serif" style="left:699px">NEWSLETTER SIGN UP</h4>
  <p class="abs news-copy">Subscribe to our newsletter to get the latest update to your inbox</p>
  <div class="abs news-input">Email address</div>
  <div class="abs news-btn">
    <svg width="14" height="14" viewBox="0 0 24 24" fill="none" stroke="#fff" stroke-width="3"><path d="M4 12h15M13 5l7 7-7 7"/></svg>
  </div>

  <div class="abs copyright">© 2024 SALTMARSH RIDGE. All Rights Reserved.</div>
</div>
</body>
</html>
```